A4 Menu needed for cafe - attached design

Need an A4 menu designed for our cafe.
I have attached our catering menu - I would like the new menu to be designed in the exact same way.

I have attached the text that needs to appear on the menu

```html
<!DOCTYPE html>
<html lang="en">
<head>
<meta charset="utf-8">
<title>Ward Nine Kitchen – Menus</title>
<link rel="stylesheet" href="https://fonts.googleapis.com/css2?family=Courier+Prime:wght@400;700&family=Oswald:wght@500&family=Lato:wght@400&display=swap">
<style>
  :root {
    --page-bg: #eceeef;
    --board: #1b1a19;
    --board-back: #161514;
    --chalk: #f1eee6;
    --line: #e9e6dc;
    --butter: #f2eca4;
    --ink: #1b1a19;
    --ribbon-shade: #c9c27c;
  }
  * { margin: 0; padding: 0; box-sizing: border-box; }
  html, body {
    width: 1200px; height: 1200px; overflow: hidden;
    background: var(--page-bg);
  }
  .sheet {
    position: absolute;
    color: var(--chalk);
    box-shadow: 0 2px 10px rgba(0,0,0,0.25);
    overflow: hidden;
  }
  .lunch-sheet { left: 52px; top: 55px; width: 945px; height: 670px; background: var(--board-back); }
  .catering-sheet { left: 200px; top: 450px; width: 950px; height: 672px; background: var(--board); }

  .ribbon { position: absolute; height: 40px; }
  .ribbon svg { position: absolute; inset: 0; width: 100%; height: 100%; }
  .ribbon span {
    position: absolute; left: 0; right: 0; top: 5px; text-align: center;
    font-family: "Oswald", sans-serif; font-weight: 500; font-size: 18px;
    color: var(--ink); letter-spacing: 0.5px; text-transform: uppercase; line-height: 24px;
  }

  .item {
    display: flex; justify-content: space-between;
    font-family: "Courier Prime", monospace; font-weight: 700;
  }
  .item-list { list-style: none; }
  .price { min-width: 40px; text-align: left; }

  /* Lunch sheet */
  .lunch-frame {
    position: absolute; left: 60px; top: 100px; width: 840px; height: 420px;
    border: 1.5px solid var(--line);
  }
  .lunch-frame .ribbon { left: -18px; top: -20px; width: 160px; }
  .lunch-col { position: absolute; top: 60px; }
  .lunch-col.left { left: 48px; width: 290px; }
  .lunch-col.right { left: 420px; width: 340px; top: 30px; }
  .lunch-col .item { font-size: 14px; line-height: 39px; }
  .lunch-col.right .item { line-height: 33px; }
  .price.wide { min-width: 90px; }

  .hot-frame {
    position: absolute; left: 60px; top: 560px; width: 400px; height: 100px;
    border: 1.5px solid var(--line);
  }
  .hot-frame .ribbon { left: -18px; top: -20px; width: 170px; }
  .hot-frame .item-list { position: absolute; left: 18px; top: 26px; width: 360px; }
  .hot-frame .item { font-size: 13px; line-height: 19px; }

  /* Catering sheet */
  .brand {
    position: absolute; top: 80px; left: 0; width: 100%;
    display: flex; justify-content: center; align-items: center; gap: 14px;
  }
  .brand-square { width: 38px; height: 38px; background: var(--butter); }
  .brand-name {
    font-family: "Courier Prime", monospace; font-weight: 700;
    font-size: 29px; letter-spacing: 2px; color: var(--butter); text-transform: uppercase;
  }
  .menu-title {
    position: absolute; top: 198px; width: 100%; text-align: center;
    font-family: "Courier Prime", monospace; font-size: 19px; color: var(--butter); letter-spacing: 1px;
  }
  .menu-section {
    position: absolute; top: 262px; width: 355px; height: 340px;
    border: 1.5px solid var(--line);
    padding: 40px 26px 0 38px;
  }
  .menu-section.breakfast { left: 108px; }
  .menu-section.light { left: 488px; }
  .menu-section .ribbon { top: -21px; left: 50%; transform: translateX(-50%); width: 190px; }
  .menu-section .item { font-size: 13.5px; line-height: 21px; }
  .light .item { line-height: 20px; }
  .footer-note {
    position: absolute; bottom: 40px; width: 100%; text-align: center;
    font-family: "Lato", sans-serif; font-size: 10px; color: var(--chalk);
  }
</style>
</head>
<body>
<svg width="0" height="0" style="position:absolute" aria-hidden="true">
  <defs>
    <symbol id="ribbon-shape" viewBox="0 0 220 46" preserveAspectRatio="none">
      <polygon points="0,12 30,12 30,44 0,44 11,28" fill="#f2eca4" stroke="#1b1a19" stroke-width="1.5"/>
      <polygon points="220,12 190,12 190,44 220,44 209,28" fill="#f2eca4" stroke="#1b1a19" stroke-width="1.5"/>
      <polygon points="16,36 30,44 30,36" fill="#c9c27c"/>
      <polygon points="204,36 190,44 190,36" fill="#c9c27c"/>
      <rect x="16" y="2" width="188" height="34" fill="#f2eca4" stroke="#1b1a19" stroke-width="1.5"/>
    </symbol>
  </defs>
</svg>

<section class="sheet lunch-sheet">
  <div class="lunch-frame">
    <div class="ribbon"><svg><use href="#ribbon-shape"/></svg><span>Lunch</span></div>
    <ul class="item-list lunch-col left">
      <li class="item"><span>Pre made Sandwiches</span><span class="price wide">$6.5/$7.5</span></li>
      <li class="item"><span>Pre made Focaccias</span><span class="price wide">$8.5</span></li>
      <li class="item"><span>Pre made Wraps</span><span class="price wide">$7.5</span></li>
      <li class="item"><span>Pre made Mini Rolls</span><span class="price wide">$4.0</span></li>
      <li class="item"><span>Pre made Baguettes</span><span class="price wide">$9.0</span></li>
      <li class="item"><span>Pre made Bagels</span><span class="price wide">$9.0</span></li>
      <li class="item"><span>Fresh Salads</span><span class="price wide">$9.5</span></li>
      <li class="item"><span>Hot Chips</span><span class="price wide">$4.0</span></li>
    </ul>
    <ul class="item-list lunch-col right">
      <li class="item"><span>Plain Hamburger</span><span class="price">$7.5</span></li>
      <li class="item"><span>Hamburger with the Lot</span><span class="price">$9.0</span></li>
      <li class="item"><span>Chicken Schnitzel Burger</span><span class="price">$8.5</span></li>
    </ul>
  </div>
  <div class="hot-frame">
    <div class="ribbon"><svg><use href="#ribbon-shape"/></svg><span>Hot Food</span></div>
    <ul class="item-list">
      <li class="item"><span>Assorted Pies</span><span class="price">$5.0</span></li>
      <li class="item"><span>Large tray Sausage Rolls</span><span class="price">$40</span></li>
      <li class="item"><span>Small tray Sausage Rolls</span><span class="price">$25</span></li>
      <li class="item"><span>Mini sliders</span><span class="price">$4.0</span></li>
    </ul>
  </div>
</section>

<main class="sheet catering-sheet">
  <div class="brand">
    <span class="brand-square"></span>
    <span class="brand-name">Ward Nine Kitchen</span>
  </div>
  <p class="menu-title">catering menu</p>

  <section class="menu-section breakfast">
    <div class="ribbon"><svg><use href="#ribbon-shape"/></svg><span>Breakfast</span></div>
    <ul class="item-list">
      <li class="item"><span>toast per slice</span><span class="price">$2</span></li>
      <li class="item"><span>raisin Toast per slice</span><span class="price">$2</span></li>
      <li class="item"><span>egg Bacon and Cheese Roll</span><span class="price">$6.5</span></li>
      <li class="item"><span>veggie Brekky Wrap</span><span class="price">$6.5</span></li>
      <li class="item"><span>ham and Cheese French Toast</span><span class="price">$6.5</span></li>
      <li class="item"><span>ham and Cheese Toastie</span><span class="price">$5.5</span></li>
      <li class="item"><span>cheese and Tomato Toastie</span><span class="price">$5.5</span></li>
      <li class="item"><span>ham and Cheese Croissant</span><span class="price">$6.5</span></li>
      <li class="item"><span>cheese and tomato Croissant</span><span class="price">$6.0</span></li>
      <li class="item"><span>ham Cheese and Tomato Toastie</span><span class="price">$6.0</span></li>
      <li class="item"><span>plain Croissant</span><span class="price">$3.5</span></li>
    </ul>
  </section>

  <section class="menu-section light">
    <div class="ribbon"><svg><use href="#ribbon-shape"/></svg><span>Something Light</span></div>
    <ul class="item-list">
      <li class="item"><span>Mixed Yoghurts</span><span class="price">$5.5</span></li>
      <li class="item"><span>Granola and Fruit Yoghurt</span><span class="price">$5.5</span></li>
      <li class="item"><span>Chia Pudding</span><span class="price">$5.5</span></li>
      <li class="item"><span>Bircher Muesli</span><span class="price">$5.5</span></li>
      <li class="item"><span>Fruit Salad</span><span class="price">$5.5</span></li>
      <li class="item"><span>Banana Bread</span><span class="price">$4.5</span></li>
      <li class="item"><span>Muffins - made fresh daily</span><span class="price">$4.0</span></li>
      <li class="item"><span>Slices</span><span class="price">$4.5</span></li>
      <li class="item"><span>Cookies</span><span class="price">$4.0</span></li>
      <li class="item"><span>Choc Crunch Energy Bite</span><span class="price">$4.0</span></li>
      <li class="item"><span>Super Crunch Energy Bite</span><span class="price">$4.0</span></li>
      <li class="item"><span>Chocolate Bar</span><span class="price">$3.0</span></li>
      <li class="item"><span>Packet of Chips</span><span class="price">$3.0</span></li>
    </ul>
  </section>

  <p class="footer-note">Visit us instore to discuss catering options, or call 0412 555 019 or email hello@wardninekitchen.com</p>
</main>
</body>
</html>
```